Deliver a professional and engaging investment propsal.

I am appealing to highend smart investors and need a high quality, engaging and formal presentation in PDF.
DropBox: https://www.filemarsh.net/sh/q8wz3kdmv2tanp7/BCxRp4LfWmZq9TnYeJ2sKo7vH?dl=0
Text for project is in Dropbox called New Proposal Final
Along with past much older attempts of this job.
Any additional ideas to enable a better outcome would be appreicated.

```html
<!DOCTYPE html>
<html lang="en">
<head>
<meta charset="utf-8">
<title>Proposal – Prairie Crest Business Park</title>
<link rel="stylesheet" href="https://fonts.googleapis.com/css2?family=Nunito:wght@800;900&family=Quicksand:wght@500;600&display=swap">
<style>
  :root {
    --lime: #b6cf35;
    --ink: #000000;
    --text: #1c1c1c;
    --paper: #ffffff;
    --wood-dark: #2b2622;
    --wood-mid: #5e544b;
    --plaque: #b9b8b4;
    --sky: #a9b6c2;
    --facade: #a8885c;
    --road: #8c8479;
  }
  * { margin: 0; padding: 0; box-sizing: border-box; }
  html, body { width: 848px; height: 1200px; overflow: hidden; background: var(--paper); }
  .page {
    position: relative;
    width: 848px;
    height: 1200px;
    overflow: hidden;
    background: var(--paper);
    font-family: "Quicksand", sans-serif;
    color: var(--text);
  }
  .backdrop { position: absolute; inset: 0; }
  .title-band {
    position: absolute;
    left: 194px; top: 228px;
    width: 345px; height: 82px;
    background: var(--lime);
  }
  .title-band h1 {
    font-family: "Nunito", sans-serif;
    font-weight: 900;
    font-size: 52px;
    line-height: 82px;
    padding-left: 28px;
    color: var(--ink);
  }
  .intro {
    position: absolute;
    left: 208px; top: 321px;
    width: 558px;
  }
  .intro p {
    font-size: 16px;
    line-height: 20.6px;
    font-weight: 500;
    text-align: justify;
    margin-bottom: 20.6px;
  }
  .intro p:first-child { padding-left: 6px; }
  .options-heading {
    position: absolute;
    left: 205px; top: 578px;
    font-family: "Nunito", sans-serif;
    font-weight: 800;
    font-size: 34px;
    line-height: 44px;
    color: var(--lime);
  }
  .options {
    position: absolute;
    left: 258px; top: 640px;
    width: 506px;
    list-style: none;
  }
  .options li {
    position: relative;
    padding-left: 48px;
    font-size: 16px;
    line-height: 20.6px;
    font-weight: 500;
    margin-bottom: 20.6px;
  }
  .options li::before {
    content: "";
    position: absolute;
    left: 0; top: 4px;
    width: 16px; height: 16px;
    border-radius: 50%;
    background: var(--lime);
  }
  .options .lead {
    font-family: "Nunito", sans-serif;
    font-weight: 800;
    font-size: 21px;
    color: var(--lime);
  }
</style>
</head>
<body>
<div class="page">
  <svg class="backdrop" width="848" height="1200" viewBox="0 0 848 1200" xmlns="http://www.w3.org/2000/svg">
    <defs>
      <linearGradient id="signTone" x1="0" y1="0" x2="0" y2="1">
        <stop offset="0" stop-color="var(--wood-mid)"/>
        <stop offset="0.14" stop-color="#8d8882"/>
        <stop offset="0.3" stop-color="var(--plaque)"/>
        <stop offset="0.5" stop-color="#9e9c98"/>
        <stop offset="0.66" stop-color="var(--wood-mid)"/>
        <stop offset="1" stop-color="var(--wood-dark)"/>
      </linearGradient>
      <linearGradient id="streetTone" x1="0" y1="0" x2="0" y2="1">
        <stop offset="0" stop-color="var(--sky)"/>
        <stop offset="0.35" stop-color="#c2c6c6"/>
        <stop offset="0.55" stop-color="var(--facade)"/>
        <stop offset="0.78" stop-color="#6f6a62"/>
        <stop offset="1" stop-color="var(--road)"/>
      </linearGradient>
    </defs>
    <rect x="0" y="0" width="848" height="300" fill="url(#signTone)" role="img" aria-label="Photo of a weathered town welcome sign mounted on old wooden boards"/>
    <path d="M0,262 Q60,240 210,212 Q450,175 848,268 L848,1200 L0,1200 Z" fill="var(--ink)"/>
    <path d="M210,212 Q450,175 848,268 L848,1200 L240,1200 Q180,900 178,620 Q178,400 210,212 Z" fill="var(--paper)"/>
    <rect x="202" y="875" width="646" height="325" fill="url(#streetTone)" role="img" aria-label="Photo of the town's main street with shopfronts, lamp posts and parked pickup trucks"/>
    <path d="M0,990 L224,1000 Q252,1100 282,1200 L0,1200 Z" fill="var(--ink)"/>
    <path d="M108,234 Q160,220 210,212 Q178,400 178,620 Q180,820 224,1000 L116,1000 Q92,620 108,234 Z" fill="var(--lime)"/>
  </svg>

  <div class="title-band"><h1>Proposal</h1></div>

  <section class="intro">
    <p>We have an incredible property, Prairie Crest Business Park, located at 1180 County Road 12 Harlan County, Stonebridge, North Dakota 58000 USA which we have fully funded with cash and now need a joint venture partner, buyer or lender to get this project to completion and producing a substantial profit we all can share.</p>
    <p>Our property is located on the best oil reserves in the world in North Dakota USA, with more oil than any other county in the Bakken Basin and with the lowest recoverable costs of $24 a barrel.</p>
    <p>We own the property and need a partner to develop the site and bring to the market at half the cost of competing business parks in the area.</p>
  </section>

  <h2 class="options-heading">Participation Options</h2>
  <ul class="options">
    <li><span class="lead">A JOINT VENTURE PARTNER</span> would support all the costs developing the property without the upfront costs of the property purchase.</li>
    <li>All sales would be split to ensure both parties are paid out in such a way that both are paid out in full at the same time then a 50/50 profit share split on all remaining sales.</li>
    <li>Contract drawn up protecting and supporting both parties on agreed terms.</li>
  </ul>
</div>
</body>
</html>
```